Mental Health Therapy Website

I need a design for a mental health therapy website. It is a private practice. The business name is Brindle Counseling, PLLC. My name is Martin Hale, LMHC, NCC, DCC. I would like some of the features/menus to be Home; Welcome/About Me, Rates and Services, Common Questions, and Contact.
If possible I would like a blog on the main page that I can update with articles I write. I would like the contact page to feature a map to my location (4318 Cedarbend Ave. E, Lakewood, WA 98499).
I would like to place a small photo of me on the Welcome/About page.
I am new to this so if I am forgetting anything, please ask me!!
I will upload my logo so you can fit it and the color scheme into the design.
Thank you so very much!

```html
<!DOCTYPE html>
<html lang="en">
<head>
<meta charset="utf-8">
<title>Brindle Counseling — Home</title>
<link href="https://fonts.googleapis.com/css2?family=Open+Sans:wght@300;400;600;700&display=swap" rel="stylesheet">
<style>
  :root {
    --brand-blue: #2b94cd;
    --brand-blue-dark: #2587bd;
    --ink: #333333;
    --nav-ink: #555555;
    --white: #ffffff;
    --rule: #d6d6d6;
    --page: #f1f1f1;
    --hero-light: #9cc4d8;
    --hero-mid: #6fa3c0;
    --hero-deep: #2f5f80;
    --logo-green: #5a9a3c;
    --logo-navy: #1f4e79;
  }
  * { box-sizing: border-box; margin: 0; padding: 0; }
  html, body { width: 1200px; height: 716px; overflow: hidden; }
  body {
    font-family: "Open Sans", Arial, sans-serif;
    background: var(--page);
    color: var(--ink);
    position: relative;
  }
  .color-strip {
    position: absolute; top: 0; left: 0; width: 1200px; height: 4px;
    background: repeating-linear-gradient(90deg,
      #e6337a 0 60px, #f7c21a 60px 120px, #3fae49 120px 180px,
      #2b94cd 180px 240px, #8e44ad 240px 300px, #f26522 300px 360px);
  }
  .site-header {
    position: absolute; top: 4px; left: 0; width: 1200px; height: 73px;
    background: var(--white);
    border-bottom: 2px solid var(--rule);
  }
  .brand {
    position: absolute; left: 96px; top: 10px;
    display: flex; align-items: center; gap: 10px;
  }
  .brand-mark {
    width: 46px; height: 46px; border-radius: 50%;
    background: var(--logo-green);
  }
  .brand-name {
    font-size: 22px; font-weight: 600; line-height: 1.05;
    color: var(--logo-navy);
  }
  .main-nav {
    position: absolute; top: 21px; left: 554px;
    display: flex; align-items: center;
  }
  .main-nav a {
    display: block; text-decoration: none;
    font-size: 11px; text-transform: uppercase;
    color: var(--nav-ink); padding: 9px 19px; line-height: 14px;
    border-radius: 3px;
  }
  .main-nav a.is-active { background: var(--brand-blue); color: var(--white); padding: 9px 18px; }
  .hero {
    position: absolute; top: 77px; left: 0; width: 1200px; height: 279px;
    background: linear-gradient(110deg, var(--hero-light) 0%, var(--hero-mid) 45%, var(--hero-deep) 80%, var(--hero-mid) 100%);
    text-align: center; color: var(--white);
  }
  .hero-title {
    position: absolute; top: 100px; left: 0; width: 100%;
    font-size: 39px; font-weight: 700; line-height: 48px;
  }
  .hero-sub {
    position: absolute; top: 151px; left: 0; width: 100%;
    font-size: 22px; font-weight: 300; line-height: 30px;
  }
  .features {
    position: absolute; top: 356px; left: 0; width: 1200px; height: 279px;
    display: flex;
  }
  .feature {
    width: 400px; height: 100%; text-align: center;
    padding: 42px 24px 0;
  }
  .feature--blue { background: var(--brand-blue); color: var(--white); }
  .feature--light { background: var(--white); color: var(--ink); }
  .feature-icon { display: block; margin: 0 auto; width: 34px; height: 36px; }
  .feature-title {
    margin-top: 16px; font-size: 24px; font-weight: 600; line-height: 30px;
  }
  .feature-text {
    margin-top: 12px; font-size: 14px; line-height: 23px;
  }
  .feature--light .feature-text { font-size: 13px; line-height: 20.5px; margin-top: 14px; }
  .btn-appointment {
    display: inline-block; margin-top: 21px;
    background: var(--brand-blue); color: var(--white);
    font-size: 11px; text-transform: uppercase; text-decoration: none;
    width: 166px; height: 31px; line-height: 31px; border-radius: 2px;
    border-bottom: 2px solid var(--brand-blue-dark);
  }
</style>
</head>
<body>
  <div class="color-strip"></div>

  <header class="site-header">
    <div class="brand">
      <span class="brand-mark"></span>
      <span class="brand-name">Brindle Counseling</span>
    </div>
    <nav class="main-nav">
      <a class="is-active" href="#">Home</a>
      <a href="#">About Me</a>
      <a href="#">Rates and Services</a>
      <a href="#">Common Questions</a>
      <a href="#">Contact</a>
    </nav>
  </header>

  <section class="hero" role="img" aria-label="Photo of a hand touching a medical monitor screen, tinted blue">
    <h1 class="hero-title">HERE IS MARTIN HALE</h1>
    <p class="hero-sub">I am a trauma certified therapist that utilizes CBT+ to assist with trauma</p>
  </section>

  <section class="features">
    <article class="feature feature--blue">
      <svg class="feature-icon" viewBox="0 0 34 36" aria-hidden="true">
        <path d="M17 2 C17 2 6 16 6 23 a11 11 0 0 0 22 0 C28 16 17 2 17 2z" fill="#ffffff"/>
        <path d="M12 24 a5 5 0 0 0 5 5" stroke="#2b94cd" stroke-width="2" fill="none" stroke-linecap="round"/>
      </svg>
      <h2 class="feature-title">PSYCHOEDUCATION</h2>
      <p class="feature-text">Lorem ipsum dolor sit amet, consectetuer adipiscing elit, sed diam nonummy nibh euismod tincidunt ut laoreet dolore magna aliquam erat volutpat. Ut wisi enim ad minim veniam, quis nostrud exerci tation.</p>
    </article>

    <article class="feature feature--light">
      <svg class="feature-icon" viewBox="0 0 34 36" aria-hidden="true">
        <circle cx="17" cy="19" r="14" fill="none" stroke="#333333" stroke-width="4"/>
        <path d="M17 11 V20 H23" fill="none" stroke="#333333" stroke-width="3.5" stroke-linecap="round"/>
      </svg>
      <h2 class="feature-title">ASK FOR SESSION</h2>
      <p class="feature-text">If you need a doctor for to consectetuer Lorem ipsum dolor, consectetur adipiscing elit. Ut volutpat eros s adipiscing elit. Ut volutpat eros sit.</p>
      <a class="btn-appointment" href="#">Make an Appointment</a>
    </article>

    <article class="feature feature--blue">
      <svg class="feature-icon" viewBox="0 0 34 36" aria-hidden="true">
        <path d="M17 2 C17 2 6 16 6 23 a11 11 0 0 0 22 0 C28 16 17 2 17 2z" fill="#ffffff"/>
        <path d="M12 24 a5 5 0 0 0 5 5" stroke="#2b94cd" stroke-width="2" fill="none" stroke-linecap="round"/>
      </svg>
      <h2 class="feature-title">THERAPY BY CBT TOOLS</h2>
      <p class="feature-text">Lorem ipsum dolor sit amet, consectetuer adipiscing elit, sed diam nonummy nibh euismod tincidunt ut laoreet dolore magna aliquam erat volutpat. Ut wisi enim ad minim veniam, quis nostrud exerci tation.</p>
    </article>
  </section>
</body>
</html>
```